Business Card Design Project

We are an agricultural business based in Brisbane.
We design, manage and operate regional saleyards. Our logo is green/silver in colour and details of our business can be found on our website www.vodemarketyards.com.au

Just wanting a corporate design for some business cards and include name, position, contact details.

Thanks

Industry/Entity Type

Business

```html
<!DOCTYPE html>
<html lang="en">
<head>
<meta charset="utf-8">
<title>Vode Market Yards – Business Card Concepts</title>
<link rel="stylesheet" href="https://fonts.googleapis.com/css2?family=Jost:wght@300;400;600&family=EB+Garamond:ital,wght@1,700&display=swap">
<style>
  :root {
    --green: #128a3e;
    --green-deep: #0b7a35;
    --green-bright: #1fb45a;
    --green-soft: #8fd07a;
    --ink: #3a3a3a;
    --paper: #ffffff;
    --stage: #ffffff;
    --card-shadow: rgba(0,0,0,0.18);
  }
  * { box-sizing: border-box; margin: 0; padding: 0; }
  html, body { width: 1200px; height: 1000px; overflow: hidden; background: var(--stage); }
  .canvas { position: relative; width: 1200px; height: 1000px; }

  .card {
    position: absolute;
    width: 360px; height: 206px;
    border-radius: 2px;
    overflow: hidden;
    box-shadow: 0 8px 24px var(--card-shadow);
    font-family: "Jost", sans-serif;
  }
  .card--light { background: var(--paper); color: var(--ink); }
  .card--green { background: linear-gradient(160deg, var(--green-bright) 0%, var(--green) 55%, var(--green-deep) 100%); color: #e9f6ec; }

  .card--a { left: 120px; top: 160px; }
  .card--b { left: 720px; top: 150px; }
  .card--c { left: 120px; top: 590px; }
  .card--d { left: 700px; top: 600px; }

  .wordmark {
    position: absolute;
    font-family: "Jost", sans-serif;
    font-weight: 600;
    font-size: 12px;
    line-height: 1.05;
    letter-spacing: 0.5px;
    text-transform: uppercase;
    color: var(--green);
    white-space: nowrap;
  }
  .card--green .wordmark { color: #ffffff; }

  .name { font-weight: 300; font-size: 14px; line-height: 1.2; white-space: nowrap; }
  .role {
    font-family: "EB Garamond", serif;
    font-style: italic; font-weight: 700;
    font-size: 12px; line-height: 1.2;
    color: var(--green);
    white-space: nowrap;
  }
  .card--green .role { color: #ffffff; }

  .contacts { list-style: none; font-weight: 300; font-size: 11px; line-height: 1.35; white-space: nowrap; }
  .contacts .label { display: inline-block; width: 20px; }

  .tagline {
    position: absolute;
    font-family: "EB Garamond", serif;
    font-style: italic; font-weight: 700;
    font-size: 11px;
    color: var(--green);
    white-space: nowrap;
  }
  .card--green .tagline { color: #e9f6ec; }

  .details { position: absolute; }

  /* card A */
  .card--a .wordmark { left: 28px; top: 92px; }
  .card--a .details { left: 160px; top: 52px; }
  .card--a .contacts { margin-top: 10px; }
  .card--a .tagline { right: 22px; bottom: 26px; }

  /* green cards */
  .pointer { position: absolute; left: 40px; top: 70px; width: 120px; height: 44px; }
  .card--b .wordmark, .card--d .wordmark { left: 24px; top: 80px; z-index: 1; }
  .card--b .details, .card--d .details { left: 178px; top: 40px; }
  .card--b .contacts, .card--d .contacts { margin-top: 14px; color: #e9f6ec; }
  .card--b .tagline, .card--d .tagline { right: 24px; bottom: 22px; }

  /* card C */
  .name-band {
    position: absolute; left: 0; top: 30px;
    width: 206px; height: 38px;
    background: var(--green);
    padding: 3px 0 0 28px;
  }
  .name-band .name { color: #e9f6ec; }
  .name-band .role { color: #ffffff; font-size: 11px; }
  .card--c .wordmark { left: 222px; top: 38px; }
  .card--c .contacts { position: absolute; left: 28px; top: 84px; }
  .card--c .tagline { right: 22px; bottom: 34px; }
</style>
</head>
<body>
<main class="canvas">

  <article class="card card--light card--a">
    <div class="wordmark">Vode Market<br>Yards</div>
    <div class="details">
      <p class="name">Daniel Whitford</p>
      <p class="role">General Manager - VMX Portfolio</p>
      <ul class="contacts">
        <li><span class="label">m.</span>0400 555 217</li>
        <li><span class="label">e.</span>daniel@vodemarketyards.com.au</li>
        <li><span class="label">w.</span>www.vodemarketyards.com.au</li>
      </ul>
    </div>
    <p class="tagline">Building better saleyards across rural Australia</p>
  </article>

  <article class="card card--green card--b">
    <svg class="pointer" viewBox="0 0 120 44" aria-hidden="true">
      <defs>
        <linearGradient id="pointerFadeB" x1="0" x2="1">
          <stop offset="0" stop-color="#ffffff" stop-opacity="0"/>
          <stop offset="1" stop-color="#8fd07a"/>
        </linearGradient>
      </defs>
      <polygon points="0,4 100,4 120,22 100,40 0,40" fill="url(#pointerFadeB)"/>
    </svg>
    <div class="wordmark">Vode Market<br>Yards</div>
    <div class="details">
      <p class="name">Daniel Whitford</p>
      <p class="role">General Manager -<br>VMX Portfolio</p>
      <ul class="contacts">
        <li><span class="label">m.</span>0400 555 217</li>
        <li><span class="label">e.</span>daniel@vodemarketyards.com.au</li>
        <li><span class="label">w.</span>www.vodemarketyards.com.au</li>
      </ul>
    </div>
    <p class="tagline">Building better saleyards across rural Australia</p>
  </article>

  <article class="card card--light card--c">
    <div class="name-band">
      <p class="name">Daniel Whitford</p>
      <p class="role">General Manager - VMX Portfolio</p>
    </div>
    <div class="wordmark">Vode Market<br>Yards</div>
    <ul class="contacts">
      <li><span class="label">m.</span>0400 555 217</li>
      <li><span class="label">e.</span>daniel@vodemarketyards.com.au</li>
      <li><span class="label">w.</span>www.vodemarketyards.com.au</li>
    </ul>
    <p class="tagline">Building better saleyards across rural Australia</p>
  </article>

  <article class="card card--green card--d">
    <svg class="pointer" viewBox="0 0 120 44" aria-hidden="true">
      <defs>
        <linearGradient id="pointerFadeD" x1="0" x2="1">
          <stop offset="0" stop-color="#ffffff" stop-opacity="0"/>
          <stop offset="1" stop-color="#8fd07a"/>
        </linearGradient>
      </defs>
      <polygon points="0,4 100,4 120,22 100,40 0,40" fill="url(#pointerFadeD)"/>
    </svg>
    <div class="wordmark">Vode Market<br>Yards</div>
    <div class="details">
      <p class="name">Daniel Whitford</p>
      <p class="role">General Manager -<br>VMX Portfolio</p>
      <ul class="contacts">
        <li><span class="label">m.</span>0400 555 217</li>
        <li><span class="label">e.</span>daniel@vodemarketyards.com.au</li>
        <li><span class="label">w.</span>www.vodemarketyards.com.au</li>
      </ul>
    </div>
    <p class="tagline">Building better saleyards across rural Australia</p>
  </article>

</main>
</body>
</html>
```